Query Paladin Powerpoint with Major Velorian Type Theme

Need powerpoint template with matching colors and different slide options. Logo and colors to be used can be found at querypaladinhq.net. Want brightly colored slide deck that is readable form the back of a room, but highlights colors. I will be incorporating Quizzle into the slides to gamify my presentations.

Target Market(s)

Tech

Industry/Entity Type

IT, specifically database, but crossing over to mental health in IT, important note this is not for a company, this is just for a professional building a brand

Font styles to use
Sans Serif

Colors
0054AA
0677BA
7BADD7
CADEEF
E8F1F8
EB3D1F
EC4F4E
F09395
F8D3D4
FCEDEE

Requirements
Must have
• My Logo in the bottom corner, front page, a thank your page, question page, content page, content page with two columns, content page with graphs, and icons to be used in the primary colors of the logos, About Me Page, Break Slides, Demo break slide
Should not have
• Lighter shades of colors, I want to pop out where colors are used, I want spacing and font size to be readable from the back of a room, most likely black text and white background

```html
<!DOCTYPE html>
<html lang="en">
<head>
<meta charset="utf-8">
<title>Query Paladin – Presentation Template</title>
<link href="https://fonts.googleapis.com/css2?family=Lexend:wght@400;500;600&family=Open+Sans:wght@400;600&family=Great+Vibes&display=swap" rel="stylesheet">
<style>
:root{
  --navy:#123d7e;
  --navy-deep:#0b2f66;
  --blue:#1f5aa6;
  --red:#e8202a;
  --red-soft:#f6c9cb;
  --ink:#3a3a3a;
  --muted:#9a9a9a;
  --paper:#ffffff;
  --stage:#ececec;
}
*{box-sizing:border-box;margin:0;padding:0}
html,body{width:720px;height:1200px;overflow:hidden}
body{background:var(--stage);font-family:"Open Sans",Arial,sans-serif;color:var(--ink);position:relative}
.slide{position:absolute;width:228px;height:160px;background:var(--paper);box-shadow:2px 3px 6px rgba(0,0,0,.25);overflow:hidden}
.slide::after{content:"";position:absolute;left:0;right:0;bottom:0;height:4px;background:var(--red)}
.slide-title{position:absolute;top:12px;left:0;right:0;text-align:center;font-family:"Lexend",Arial,sans-serif;font-weight:600;font-size:11px;color:var(--navy);letter-spacing:.2px}
.slide-title .accent{color:var(--red)}
.brand{position:absolute;right:8px;bottom:9px;display:flex;align-items:center;gap:2px;font-family:"Lexend",Arial,sans-serif;font-weight:600;font-size:6px;color:var(--navy)}
.brand .dot{width:6px;height:6px;border-radius:50%;background:var(--red)}
.brand.light{color:#fff}
.body-text{font-size:3.4px;line-height:1.45;text-align:justify;color:var(--ink)}
.body-text p{margin-bottom:3px}

/* cover */
.cover{background:linear-gradient(160deg,var(--navy) 0%,var(--navy-deep) 100%)}
.cover .red-band{position:absolute;left:0;right:0;bottom:0;height:35px;background:var(--red)}
.cover .name-plate{position:absolute;left:54px;top:110px;width:120px;height:30px;background:#fff;outline:1px solid #fff;outline-offset:1.5px;display:flex;align-items:center;justify-content:center;gap:4px;font-family:"Lexend",Arial,sans-serif;font-weight:600;font-size:9px;color:var(--navy)}
.cover .name-plate .dot{width:8px;height:8px;border-radius:50%;background:var(--red)}

/* thank you */
.thanks{background:linear-gradient(160deg,var(--blue) 0%,var(--navy) 55%,var(--navy-deep) 100%)}
.thanks .backdrop{position:absolute;inset:0 0 4px 0;background:radial-gradient(circle at 70% 30%,rgba(80,130,205,.35) 0%,rgba(18,61,126,0) 60%)}
.thanks .script{position:absolute;left:40px;top:86px;font-family:"Great Vibes",cursive;font-size:22px;color:#fff}

/* question */
.question-list{position:absolute;left:10px;top:30px;display:flex;flex-direction:column;gap:6px}
.question-chip{width:22px;height:22px;border-radius:50%;border:1px dashed var(--red);display:flex;align-items:center;justify-content:center;padding-left:5px;font-family:"Lexend",Arial,sans-serif;font-size:2.8px;color:var(--navy);text-align:center;line-height:1.15;position:relative}
.question-chip b{position:absolute;left:1.5px;top:5px;color:var(--red);font-size:8px;font-weight:600;line-height:1}
.question-art{position:absolute;right:8px;top:2px;width:58px;height:92px;background:linear-gradient(180deg,#fbe6e6,#fdf3f3);border-radius:4px}

/* content */
.content-single .body-text{position:absolute;left:12px;right:12px;top:32px}
.two-col .col-left{position:absolute;left:8px;top:32px;width:82px}
.two-col .col-right{position:absolute;left:96px;top:32px;width:122px}
.server-art{position:absolute;left:8px;top:86px;width:84px;height:60px;background:linear-gradient(135deg,#3d6fc2,var(--navy) 60%,var(--red));border-radius:3px}

/* graph */
.graph-legend{position:absolute;left:8px;top:34px;width:36px}
.graph-legend h4{font-family:"Lexend",Arial,sans-serif;font-weight:500;font-size:3.6px;margin-top:3px}
.graph-legend h4.blue{color:var(--navy)}
.graph-legend h4.red{color:var(--red)}
.graph-legend p{font-size:2.5px;line-height:1.3;color:var(--ink)}
.graph-plot{position:absolute;left:48px;top:34px;width:172px;height:108px}

/* content & icons */
.icons-split .section-head{position:absolute;left:18px;top:32px;font-family:"Lexend",Arial,sans-serif;font-weight:500;font-size:6px;color:var(--navy)}
.feature{position:absolute;width:80px}
.feature h5{font-family:"Lexend",Arial,sans-serif;font-weight:500;font-size:4px;color:var(--red);display:flex;align-items:center;gap:3px;border-bottom:.5px solid #bbb;padding-bottom:1.5px}
.feature h5 i{width:5px;height:5px;border:.8px solid var(--red);display:inline-block}
.feature p{font-size:2.8px;line-height:1.35;color:var(--muted);margin-top:2px;padding-left:8px}
.icon-band{position:absolute;left:0;right:0;bottom:0;height:44px;background:var(--red);border-top:2px solid var(--navy);display:flex;justify-content:space-around;align-items:center;padding-top:2px}
.icon-band .cell{width:40px;text-align:center;color:#fff;font-size:2.4px;line-height:1.3}
.icon-band svg{width:11px;height:11px;display:block;margin:0 auto 4px}

/* icons page */
.icon-grid{position:absolute;left:10px;right:10px;top:38px;display:grid;grid-template-columns:repeat(6,1fr);row-gap:10px}
.icon-item{text-align:center;font-family:"Lexend",Arial,sans-serif;font-size:3px;line-height:1.2;color:var(--navy)}
.icon-item svg{width:14px;height:14px;display:block;margin:0 auto 3px}
.icon-item span{color:var(--red);display:block}

/* about */
.about .portrait{position:absolute;left:8px;top:30px;width:36px;height:36px;background:linear-gradient(135deg,#4a7bd0,#c0304a 60%,#5a5a5a);border-radius:2px}
.about .bio-top{position:absolute;left:48px;right:10px;top:30px}
.about .bio-bottom{position:absolute;left:12px;right:10px;top:70px}
.about .emblem{position:absolute;left:74px;top:118px;width:80px;text-align:center;font-family:"Lexend",Arial,sans-serif;font-weight:600;font-size:9px;color:var(--navy);display:flex;align-items:center;justify-content:center;gap:3px}
.about .emblem .dot{width:10px;height:10px;border-radius:50%;background:var(--red)}

/* break */
.break .towers-art{position:absolute;left:24px;top:34px;width:180px;height:110px;background:radial-gradient(ellipse at 50% 50%,#f1c7c9 0%,#e9eef6 55%,#fff 80%)}

/* contact */
.contact{background:linear-gradient(180deg,#6b7a99 0%,#3e4c6b 55%,#2a3552 100%)}
.contact .city-art{position:absolute;inset:0 0 28px 0}
.contact .center-name{position:absolute;left:0;right:0;top:52px;display:flex;justify-content:center;align-items:center;gap:5px;font-family:"Lexend",Arial,sans-serif;font-weight:600;font-size:14px;color:#fff}
.contact .center-name .dot{width:14px;height:14px;border-radius:50%;background:#fff}
.contact .info-bar{position:absolute;left:0;right:0;bottom:0;height:28px;background:var(--red);display:flex;align-items:center;justify-content:space-around;padding:0 8px;z-index:2}
.contact .info{display:flex;align-items:center;gap:3px;color:#fff;font-size:3px;line-height:1.35;letter-spacing:.3px}
.contact .info .pin{width:7px;height:7px;border-radius:50%;background:#fff;display:flex;align-items:center;justify-content:center}
</style>
</head>
<body>

<!-- Cover -->
<section class="slide cover" style="left:246px;top:50px">
  <div class="red-band"></div>
  <div class="name-plate"><span class="dot"></span>Query Paladin</div>
</section>

<!-- Thank you -->
<section class="slide thanks" style="left:9px;top:270px">
  <div class="backdrop" role="img" aria-label="Soft blue tech backdrop with faint connected lines and cubes"></div>
  <div class="script">Thank you</div>
  <div class="brand light"><span class="dot"></span>Query Paladin</div>
</section>

<!-- Question page -->
<section class="slide" style="left:246px;top:270px">
  <h2 class="slide-title">QUESTION <span class="accent">PAGE</span></h2>
  <div class="question-art" role="img" aria-label="Faint decorative question marks"></div>
  <div class="question-list">
    <div class="question-chip"><b>?</b>QUESTION<br>01</div>
    <div class="question-chip"><b>?</b>QUESTION<br>02</div>
    <div class="question-chip"><b>?</b>QUESTION<br>03</div>
    <div class="question-chip"><b>?</b>QUESTION<br>04</div>
  </div>
  <div class="brand"><span class="dot"></span>Query Paladin</div>
</section>

<!-- Content page -->
<section class="slide content-single" style="left:483px;top:270px">
  <h2 class="slide-title">CONTENT <span class="accent">PAGE</span></h2>
  <div class="body-text">
    <p>Lorem ipsum dolor sit amet, consectetuer adipiscing elit, sed diam nonummy nibh euismod tincidunt ut laoreet dolore magna aliquam erat volutpat. Ut wisi enim ad minim veniam, quis nostrud exerci tation ullamcorper suscipit lobortis nisl ut aliquip ex ea commodo consequat. Duis autem vel eum iriure dolor in hendrerit in vulputate velit esse molestie consequat, vel illum dolore eu feugiat nulla facilisis at vero eros et accumsan et iusto odio dignissim qui blandit praesent luptatum zzril delenit augue duis dolore te feugait nulla facilisi.</p>
    <p>Lorem ipsum dolor sit amet, cons ectetuer adipiscing elit, sed diam nonummy nibh euismod tincidunt ut laoreet dolore magna aliquam erat volutpat. Ut wisi enim ad minim veniam, quis nostrud exerci tation ullamcorper suscipit lobortis nisl ut aliquip ex ea commodo consequat.</p>
    <p>Lorem ipsum dolor sit amet, consectetuer adipiscing elit, sed diam nonummy nibh euismod tincidunt ut laoreet dolore magna aliquam erat volutpat. Ut wisi enim ad minim veniam, quis nostrud exerci tation ullamcorper suscipit lobortis nisl ut aliquip ex ea commodo consequat. Duis autem vel eum iriure dolor in hendrerit in vulputate velit esse molestie consequat, vel illum dolore eu feugiat nulla facilisis at vero eros et accumsan et iusto odio dignissim qui blandit praesent luptatum zzril delenit augue duis dolore te feugait nulla facilisi.</p>
  </div>
  <div class="brand"><span class="dot"></span>Query Paladin</div>
</section>

<!-- Content two columns -->
<section class="slide two-col" style="left:9px;top:490px">
  <h2 class="slide-title">CONTENT <span class="accent">PAGE</span></h2>
  <div class="body-text col-left">
    <p>Lorem ipsum dolor sit amet, consectetuer adipiscing elit, sed diam nonummy nibh euismod tincidunt ut laoreet dolore magna aliquam erat volutpat. Ut wisi enim ad minim veniam, quis nostrud exerci tation ullamcorper suscipit lobortis nisl ut aliquip ex ea commodo consequat.</p>
    <p>Duis autem vel eum iriure dolor in hendrerit in vulputate velit esse molestie consequat, vel illum dolore eu feugiat.</p>
  </div>
  <div class="server-art" role="img" aria-label="Isometric illustration of server racks with engineers"></div>
  <div class="body-text col-right">
    <p>Lorem ipsum dolor sit amet, consectetuer adipiscing elit, sed diam nonummy nibh euismod tincidunt ut laoreet dolore magna aliquam erat volutpat. Ut wisi enim ad minim veniam, quis nostrud exerci tation ullamcorper suscipit lobortis nisl ut aliquip ex ea commodo consequat. Duis autem vel eum iriure dolor in hendrerit in vulputate velit esse molestie consequat, vel illum dolore eu feugiat nulla facilisis at vero eros et accumsan et iusto odio dignissim qui blandit praesent luptatum zzril delenit augue duis dolore te feugait nulla facilisi.</p>
    <p>Lorem ipsum dolor sit amet, consectetuer adipiscing elit, sed diam nonummy nibh euismod tincidunt ut laoreet dolore magna aliquam erat volutpat. Ut wisi enim ad minim veniam, quis nostrud exerci tation ullamcorper suscipit lobortis nisl ut aliquip ex ea commodo consequat. Duis autem vel eum iriure dolor in hendrerit in vulputate velit esse molestie consequat, vel illum dolore eu feugiat nulla facilisis at vero eros et accumsan et iusto odio dignissim qui blandit praesent luptatum zzril delenit augue duis dolore te feugait nulla facilisi.</p>
  </div>
  <div class="brand"><span class="dot"></span>Query Paladin</div>
</section>

<!-- Graphs -->
<section class="slide" style="left:246px;top:490px">
  <h2 class="slide-title">CONTENT PAGE <span class="accent">WITH GRAPHS</span></h2>
  <div class="graph-legend">
    <h4 class="blue">Title One</h4><p>Nam pretium turpis et arcu. Duis arcu tortor, suscipit eget, imperdiet nec.</p>
    <h4 class="red">Title Two</h4><p>Nam pretium turpis et arcu. Duis arcu tortor, suscipit eget, imperdiet nec.</p>
    <h4 class="blue">Title Three</h4><p>Nam pretium turpis et arcu. Duis arcu tortor, suscipit eget, imperdiet nec.</p>
    <h4 class="red">Title Four</h4><p>Nam pretium turpis et arcu. Duis arcu tortor, suscipit eget, imperdiet nec.</p>
  </div>
  <svg class="graph-plot" viewBox="0 0 172 108" aria-label="Line chart of four series, 2010 to 2020">
    <g stroke="#e2e2e2" stroke-width=".4">
      <line x1="20" y1="4" x2="20" y2="96"/><line x1="35" y1="4" x2="35" y2="96"/><line x1="50" y1="4" x2="50" y2="96"/><line x1="65" y1="4" x2="65" y2="96"/><line x1="80" y1="4" x2="80" y2="96"/><line x1="95" y1="4" x2="95" y2="96"/><line x1="110" y1="4" x2="110" y2="96"/><line x1="125" y1="4" x2="125" y2="96"/><line x1="140" y1="4" x2="140" y2="96"/><line x1="155" y1="4" x2="155" y2="96"/><line x1="170" y1="4" x2="170" y2="96"/>
    </g>
    <g font-family="Lexend,sans-serif" font-size="3.5" fill="#9a9a9a" text-anchor="end">
      <text x="17" y="12">2020</text><text x="17" y="27">2018</text>
      <text x="17" y="42" fill="#123d7e">2016</text><text x="17" y="57" fill="#123d7e">2014</text>
      <text x="17" y="72" fill="#123d7e">2012</text><text x="17" y="87" fill="#e8202a">2010</text>
    </g>
    <g font-family="Lexend,sans-serif" font-size="3.2" fill="#9a9a9a" text-anchor="middle">
      <text x="20" y="102">0</text><text x="35" y="102">10</text><text x="50" y="102">20</text><text x="65" y="102">30</text><text x="80" y="102">40</text><text x="95" y="102">50</text><text x="110" y="102">60</text><text x="125" y="102">70</text><text x="140" y="102">80</text><text x="155" y="102">90</text><text x="170" y="102">100</text>
    </g>
    <g fill="none" stroke-width=".9">
      <path stroke="#123d7e" d="M20 42 C40 28 55 18 80 12 C100 6 110 14 125 18 C140 22 155 16 170 10"/>
      <path stroke="#e8202a" d="M20 58 C40 48 60 40 80 42 C100 44 115 52 130 54 C145 56 158 58 170 60"/>
      <path stroke="#123d7e" d="M20 72 C40 62 60 56 80 58 C95 62 105 70 115 66 C135 60 150 50 170 42"/>
      <path stroke="#e8202a" d="M20 86 C40 84 55 80 70 74 C90 68 105 64 120 66 C140 70 158 80 170 86"/>
    </g>
    <g fill="#123d7e">
      <circle cx="20" cy="42" r="1.3"/><circle cx="50" cy="22" r="1.3"/><circle cx="80" cy="12" r="1.3"/><circle cx="125" cy="18" r="1.3"/><circle cx="170" cy="10" r="1.3"/>
      <circle cx="20" cy="72" r="1.3"/><circle cx="80" cy="58" r="1.3"/><circle cx="115" cy="66" r="1.3"/><circle cx="170" cy="42" r="1.3"/>
    </g>
    <g fill="#e8202a">
      <circle cx="20" cy="58" r="1.3"/><circle cx="80" cy="42" r="1.3"/><circle cx="130" cy="54" r="1.3"/><circle cx="170" cy="60" r="1.3"/>
      <circle cx="20" cy="86" r="1.3"/><circle cx="70" cy="74" r="1.3"/><circle cx="120" cy="66" r="1.3"/><circle cx="170" cy="86" r="1.3"/>
    </g>
  </svg>
  <div class="brand"><span class="dot"></span>Query Paladin</div>
</section>

<!-- Content & icons -->
<section class="slide icons-split" style="left:483px;top:490px">
  <h2 class="slide-title">CONTENT &amp; <span class="accent">ICONS PAGE</span></h2>
  <div class="section-head">HEADING HERE</div>
  <div class="feature" style="left:18px;top:42px"><h5><i></i>HEADING HERE</h5><p>Lorem ipsum dolor sit amet, consec tetuer adipiscing elit, sed diam nonummy nibh euismod tincidunt ut laoreet dolore magna aliquam erat</p></div>
  <div class="feature" style="left:122px;top:42px"><h5><i></i>HEADING HERE</h5><p>Lorem ipsum dolor sit amet, consec tetuer adipiscing elit, sed diam nonummy nibh euismod tincidunt ut laoreet dolore magna aliquam erat</p></div>
  <div class="feature" style="left:18px;top:76px"><h5><i></i>HEADING HERE</h5><p>Lorem ipsum dolor sit amet, consec tetuer adipiscing elit, sed diam nonummy nibh euismod tincidunt ut laoreet dolore magna aliquam erat</p></div>
  <div class="feature" style="left:122px;top:76px"><h5><i></i>HEADING HERE</h5><p>Lorem ipsum dolor sit amet, consec tetuer adipiscing elit, sed diam nonummy nibh euismod tincidunt ut laoreet dolore magna aliquam erat</p></div>
  <div class="icon-band">
    <div class="cell"><svg viewBox="0 0 12 12" fill="none" stroke="#fff" stroke-width=".7"><path d="M6 1 C8 3 8 6 7.5 8 H4.5 C4 6 4 3 6 1Z M4.5 8 L3.5 10 M7.5 8 L8.5 10"/><circle cx="6" cy="5" r=".9"/></svg>Lorem ipsum dolor sit amet, consectetuer adipiscing elit</div>
    <div class="cell"><svg viewBox="0 0 12 12" fill="none" stroke="#fff" stroke-width=".7"><circle cx="6" cy="5" r="3"/><path d="M4.8 8 V9.5 H7.2 V8 M6 0.5 V1 M1.5 5 H1 M11 5 H10.5"/></svg>Lorem ipsum dolor sit amet, consectetuer adipiscing elit</div>
    <div class="cell"><svg viewBox="0 0 12 12" fill="none" stroke="#fff" stroke-width=".7"><circle cx="6" cy="6" r="2"/><circle cx="6" cy="6" r="4" stroke-dasharray="1.6 1"/></svg>Lorem ipsum dolor sit amet, consectetuer adipiscing elit</div>
    <div class="cell"><svg viewBox="0 0 12 12" fill="#fff"><rect x="1" y="8" width="1.4" height="3"/><rect x="3.2" y="7" width="1.4" height="4"/><rect x="5.4" y="5.5" width="1.4" height="5.5"/><rect x="7.6" y="4" width="1.4" height="7"/><rect x="9.8" y="2" width="1.4" height="9"/></svg>Lorem ipsum dolor sit amet, consectetuer adipiscing elit</div>
  </div>
</section>

<!-- Icons page -->
<section class="slide" style="left:9px;top:710px">
  <h2 class="slide-title">ICONS <span class="accent">PAGE</span></h2>
  <div class="icon-grid">
    <div class="icon-item"><svg viewBox="0 0 14 14" fill="none" stroke="#123d7e" stroke-width=".8"><rect x="1" y="2" width="9" height="6"/><circle cx="10" cy="9" r="2.2" stroke="#e8202a"/><path d="M11.6 10.6 L13 12" stroke="#e8202a"/></svg>TEXT HERE<span>TEXT HERE<br>HERE</span></div>
    <div class="icon-item"><svg viewBox="0 0 14 14" fill="none" stroke="#e8202a" stroke-width=".8"><circle cx="7" cy="7" r="4"/><path d="M7 1 V13 M1 7 H13" stroke="#123d7e"/></svg>TEXT HERE<span>TEXT HERE<br>HERE</span></div>
    <div class="icon-item"><svg viewBox="0 0 14 14" fill="none" stroke="#e8202a" stroke-width=".8"><path d="M1 10 L4 5 L7 8 L10 3 L13 6"/><circle cx="10" cy="10" r="2" stroke="#123d7e"/></svg>TEXT HERE<span>TEXT HERE<br>HERE</span></div>
    <div class="icon-item"><svg viewBox="0 0 14 14" fill="none" stroke="#123d7e" stroke-width=".8"><ellipse cx="7" cy="2.5" rx="2.5" ry="1"/><path d="M4.5 2.5 V6 C4.5 7 9.5 7 9.5 6 V2.5 M7 7 V9 M2 11 H12"/><circle cx="2.5" cy="12" r="1" stroke="#e8202a"/><circle cx="7" cy="12" r="1" stroke="#e8202a"/><circle cx="11.5" cy="12" r="1" stroke="#e8202a"/></svg>TEXT HERE<span>TEXT HERE<br>HERE</span></div>
    <div class="icon-item"><svg viewBox="0 0 14 14" fill="none" stroke="#123d7e" stroke-width=".8"><path d="M3 8 C1 8 1 5 3.5 5 C4 2 9 2 9.5 5 C12.5 5 12.5 8 10.5 8 Z"/><path d="M5 8 V11 M7 8 V12 M9 8 V11" stroke="#e8202a"/></svg>TEXT HERE<span>TEXT HERE<br>HERE</span></div>
    <div class="icon-item"><svg viewBox="0 0 14 14" fill="none" stroke="#123d7e" stroke-width=".8"><ellipse cx="7" cy="2.5" rx="4" ry="1.4"/><path d="M3 2.5 V11.5 C3 13 11 13 11 11.5 V2.5 M3 6 C3 7.4 11 7.4 11 6 M3 9 C3 10.4 11 10.4 11 9" stroke="#e8202a"/></svg>TEXT HERE<span>TEXT HERE<br>HERE</span></div>
    <div class="icon-item"><svg viewBox="0 0 14 14" fill="none" stroke="#123d7e" stroke-width=".8"><rect x="1" y="1" width="12" height="4"/><path d="M4 5 V8 M10 5 V8" stroke="#e8202a"/><circle cx="4" cy="10" r="2" stroke="#e8202a"/><circle cx="10" cy="10" r="2"/></svg>TEXT HERE<span>TEXT HERE<br>HERE</span></div>
    <div class="icon-item"><svg viewBox="0 0 14 14" fill="none" stroke="#e8202a" stroke-width=".8"><path d="M3 6 C1 6 1 3 3.5 3 C4 0.5 9 0.5 9.5 3 C12.5 3 12.5 6 10.5 6 Z"/><rect x="3" y="8" width="8" height="4" stroke="#123d7e"/></svg>TEXT HERE<span>TEXT HERE<br>HERE</span></div>
    <div class="icon-item"><svg viewBox="0 0 14 14" fill="none" stroke="#123d7e" stroke-width=".8"><rect x="3.5" y="3.5" width="7" height="7"/><rect x="5.5" y="5.5" width="3" height="3" stroke="#e8202a"/><path d="M5 1 V3.5 M9 1 V3.5 M5 10.5 V13 M9 10.5 V13 M1 5 H3.5 M1 9 H3.5 M10.5 5 H13 M10.5 9 H13"/></svg>TEXT HERE<span>TEXT HERE<br>HERE</span></div>
    <div class="icon-item"><svg viewBox="0 0 14 14" fill="none" stroke="#123d7e" stroke-width=".8"><path d="M1 4 H13 L8 9 V13 L6 12 V9 Z"/><path d="M4 1 V3 M7 1 V3 M10 1 V3" stroke="#e8202a"/></svg>TEXT HERE<span>TEXT HERE<br>HERE</span></div>
    <div class="icon-item"><svg viewBox="0 0 14 14" fill="none" stroke="#123d7e" stroke-width=".8"><rect x="1.5" y="1.5" width="11" height="11"/><path d="M1.5 5 H12.5 M1.5 8.5 H12.5" /><path d="M3.5 3.2 H6 M3.5 6.8 H6 M3.5 10.5 H6" stroke="#e8202a"/></svg>TEXT HERE<span>TEXT HERE<br>HERE</span></div>
    <div class="icon-item"><svg viewBox="0 0 14 14" fill="none" stroke="#123d7e" stroke-width=".8"><circle cx="6" cy="7" r="4.5"/><path d="M6 7 L6 2.5 M6 7 L10 9" stroke="#e8202a"/><path d="M11 3 H13.5 M11 5 H13.5" stroke="#e8202a"/></svg>TEXT HERE<span>TEXT HERE<br>HERE</span></div>
  </div>
  <div class="brand"><span class="dot"></span>Query Paladin</div>
</section>

<!-- About -->
<section class="slide about" style="left:246px;top:710px">
  <h2 class="slide-title">ABOUT <span class="accent">US</span></h2>
  <div class="portrait" role="img" aria-label="Portrait photo of the presenter"></div>
  <div class="body-text bio-top"><p>Dana Whitfield is currently a Data Community Fellow, Spark Community Award winner, and works as a Senior Database Administrator for SignLedger. Dana has worked on relational servers for many years. She is currently a co-leader of the Piedmont Data User Group in Raleigh, NC. Dana tinkered with databases in middle school to keep her sports card collection organized and got an early start on databases.</p></div>
  <div class="body-text bio-bottom">
    <p>When not doing things in the data community she likes to be somewhere making a difference. Her passion outside of databases is volunteering by advocating for abused and neglected foster children in court through the County Child Advocate program, where she has advocated for over 60 children. As someone who experienced mental health issues she has for the past two years started being a mental health advocate by being a part of the PAMH Council and the Rights Network of the Carolinas Advisory Council.</p>
    <p>You may reach me by messaging me on Chirper.</p>
  </div>
  <div class="emblem"><span class="dot"></span>Query Paladin</div>
  <div class="brand"><span class="dot"></span>Query Paladin</div>
</section>

<!-- Break -->
<section class="slide break" style="left:483px;top:710px">
  <h2 class="slide-title">BREAK <span class="accent">SLIDES</span></h2>
  <div class="towers-art" role="img" aria-label="Isometric illustration of red and white data towers with small figures"></div>
  <div class="brand"><span class="dot"></span>Query Paladin</div>
</section>

<!-- Contact -->
<section class="slide contact" style="left:246px;top:930px">
  <div class="city-art" role="img" aria-label="Dusky city skyline photo with cloud and signal line icons"></div>
  <div class="center-name"><span class="dot"></span>Query Paladin</div>
  <div class="info-bar">
    <div class="info"><span class="pin"><svg width="4" height="4" viewBox="0 0 4 4"><path d="M2 .3 C3.2 .3 3.4 1.8 2 3.7 C.6 1.8 .8 .3 2 .3Z" fill="#e8202a"/></svg></span><span>Your Address Here<br>Lorem Ipsum<br>Dolor Sit Amet</span></div>
    <div class="info"><span class="pin"><svg width="4" height="4" viewBox="0 0 4 4"><path d="M.6 .6 L1.4 .4 L1.8 1.4 L1.3 1.8 C1.6 2.4 1.9 2.7 2.4 2.9 L2.8 2.4 L3.7 2.8 L3.4 3.6 C1.8 3.5 .5 2.2 .6 .6Z" fill="#e8202a"/></svg></span><span>Phone : +01 555 01234<br>Fax &nbsp;&nbsp;&nbsp;: +01 555 01235</span></div>
    <div class="info"><span class="pin"><svg width="4" height="4" viewBox="0 0 4 4"><circle cx="2" cy="2" r="1.5" fill="none" stroke="#e8202a" stroke-width=".5"/></svg></span><span>Email : hello@querypaladinhq.net<br>Web &nbsp;: querypaladinhq.net</span></div>
  </div>
</section>

</body>
</html>
```